Website Design for Trading Company

Website for a trading company. No e-commerce required but dues need an AI Bot for questions, and needs to look extremely professional. Some examples of similar websites are:
selvanmilk(dot)com
brakomel(dot)com
tovirex(dot)com
pkrcream(dot)com(dot)au

Colour theme and style can be viewed in the files below.

Target Market(s)

Business to Business

Industry/Entity Type

Dairy Trading Business

Coding

Coded - Design and coding required

Number of Pages Required

5+ page

Font styles to use
Serif
Sans Serif

Colors
0054AA
0677BA
7BADD7
CADEEF
E8F1F8
00AB8E
00BBA5
67D7C9
C6EFE9
E9F9F6
59FF00
82FF00
B8FF75
E3FFCB
F4FFEA

Requirements
Nice to have
• AI Bot

```html
<!DOCTYPE html>
<html lang="en">
<head>
<meta charset="utf-8">
<title>Verdale Trade – Dairy Trading</title>
<link href="https://fonts.googleapis.com/css2?family=Poppins:wght@400;500;600;700;800&display=swap" rel="stylesheet">
<style>
:root{
  --navy:#0054AA;
  --blue:#0677BA;
  --sky:#7BADD7;
  --mist:#CADEEF;
  --teal:#00AB8E;
  --teal-2:#00BBA5;
  --teal-3:#67D7C9;
  --teal-pale:#E9F9F6;
  --green:#3DB54A;
  --ink:#333;
  --white:#fff;
}
*{box-sizing:border-box;margin:0;padding:0}
html,body{width:1200px;height:4800px;overflow:hidden}
body{position:relative;font-family:"Poppins",sans-serif;color:var(--ink);background:var(--white)}
.abs{position:absolute}
.brand{display:flex;align-items:center;gap:12px;font-family:"Poppins",sans-serif;font-weight:700;color:var(--navy);font-size:38px;line-height:1}
.brand-mark{width:14px;height:14px;border-radius:50%;background:var(--navy)}
.contact-item{display:flex;align-items:center;gap:14px}
.contact-icon{width:46px;height:46px;border-radius:50%;background:var(--navy);display:flex;align-items:center;justify-content:center}
.contact-label{font-size:14px;font-weight:600;color:var(--navy);line-height:1.2}
.contact-value{font-size:26px;font-weight:700;color:var(--teal);line-height:1.1}
.contact-value.small{font-size:18px;font-weight:500}
.nav{top:106px;left:0;width:1200px;height:56px;background:var(--blue)}
.nav ul{list-style:none;display:flex;gap:38px;position:absolute;left:73px;top:20px}
.nav li{color:#fff;font-size:13px;font-weight:600;text-transform:uppercase}
.login{position:absolute;right:0;top:0;height:56px;width:220px;background:var(--teal);clip-path:polygon(24px 0,100% 0,100% 100%,0 100%);color:#fff;font-size:13px;font-weight:600;display:flex;align-items:center;justify-content:center;gap:8px}
.hero{top:162px;left:0;width:1200px;height:710px;background:linear-gradient(120deg,#8a8f8c 0%,#c9cdd0 40%,#e4e8ea 70%,#b4bcc2 100%)}
.hero-text{position:absolute;left:0;width:1200px;text-align:center;color:#fff;font-weight:800;line-height:1;text-shadow:0 2px 10px rgba(0,0,0,.25)}
.btn{display:inline-flex;align-items:center;justify-content:center;background:var(--teal);color:#fff;font-weight:600;border-radius:30px}
.dot{width:14px;height:14px;border-radius:50%;background:#fff}
.section-title{font-weight:800;color:var(--navy);line-height:1.1}
.body-text{font-size:15px;line-height:29px;color:#444}
.photo{background:linear-gradient(135deg,#d9c7a0,#f2e6cc 50%,#9aa875)}
.band{background:var(--teal-pale)}
.service{position:absolute;width:240px;text-align:center}
.service .circle{width:220px;height:220px;border-radius:50%;margin:0 auto}
.service h3{margin-top:32px;font-size:22px;font-weight:700;color:var(--blue)}
.why{position:absolute;width:240px;text-align:center}
.why .ring{width:130px;height:130px;border-radius:50%;border:2px solid var(--blue);margin:0 auto;display:flex;align-items:center;justify-content:center}
.why h3{margin-top:26px;font-size:23px;font-weight:700;color:var(--teal)}
.why p{font-size:14.5px;line-height:25px;color:#444;margin-top:4px}
.news{position:absolute;width:330px}
.news .thumb{height:224px}
.news h3{margin-top:34px;font-size:26px;font-weight:500;line-height:32px;color:var(--blue)}
.news .date{font-size:13px;font-weight:700;color:var(--teal);margin-top:10px}
.news p{font-size:14.5px;line-height:28px;color:#444;margin-top:6px}
.field{position:absolute;background:#fff;border-radius:30px;font-size:14px;color:#555;padding-left:24px;display:flex;align-items:center}
.footer-col h4{font-size:22px;font-weight:600;color:var(--blue);margin-bottom:14px}
.footer-col li{list-style:none;font-size:14.5px;line-height:33px;color:#333}
.social{width:26px;height:26px;border-radius:50%;background:#222}
</style>
</head>
<body>

<header>
  <div class="abs brand" style="left:75px;top:34px"><span class="brand-mark"></span>Verdale Trade</div>
  <div class="abs contact-item" style="left:498px;top:30px">
    <div class="contact-icon"><svg width="22" height="22" viewBox="0 0 24 24"><path fill="#fff" d="M6.6 10.8a15 15 0 0 0 6.6 6.6l2.2-2.2c.3-.3.7-.4 1-.2 1.1.4 2.3.6 3.6.6.6 0 1 .4 1 1V20c0 .6-.4 1-1 1C10.6 21 3 13.4 3 4c0-.6.4-1 1-1h3.5c.6 0 1 .4 1 1 0 1.3.2 2.5.6 3.6.1.3 0 .7-.2 1z"/></svg></div>
    <div><div class="contact-label">CALL US</div><div class="contact-value">+61 3 5550 0142</div></div>
  </div>
  <div class="abs contact-item" style="left:826px;top:30px">
    <div class="contact-icon"><svg width="22" height="22" viewBox="0 0 24 24"><path fill="#fff" d="M3 5h18v14H3z"/><path fill="none" stroke="#0054AA" stroke-width="2" d="M3 6l9 7 9-7"/></svg></div>
    <div><div class="contact-label">EMAIL US</div><div class="contact-value small">sales@verdaletrade.com</div></div>
  </div>
</header>

<nav class="abs nav">
  <ul><li>Home</li><li>About Us</li><li>Service Offering</li><li>Products</li><li>Latest News</li><li>Contact Us</li></ul>
  <div class="login"><svg width="14" height="14" viewBox="0 0 24 24"><circle cx="12" cy="7" r="5" fill="#fff"/><path fill="#fff" d="M2 23c0-6 4.5-9 10-9s10 3 10 9z"/></svg>USER LOGIN</div>
</nav>

<section class="abs hero" role="img" aria-label="Hand picking a bottle of milk from a supermarket dairy shelf">
  <div class="hero-text" style="top:128px;font-size:70px">Welcome to</div>
  <div class="hero-text" style="top:190px;font-size:104px">Verdale Trade</div>
  <div class="hero-text" style="top:311px;font-size:60px">Feeding The Future</div>
  <div class="abs" style="left:512px;top:418px"><span class="btn" style="width:176px;height:54px;font-size:20px">Read More</span></div>
  <div class="abs" style="left:73px;top:547px;display:flex;gap:12px"><span class="dot" style="background:var(--blue)"></span><span class="dot"></span><span class="dot"></span><span class="dot"></span></div>
</section>
<svg class="abs" style="left:0;top:780px" width="1200" height="100" viewBox="0 0 1200 100">
  <path d="M20 75 C300 20 500 30 700 50 C900 70 1050 60 1200 40 L1200 100 L20 100 Z" fill="var(--teal)"/>
  <path d="M20 90 C300 40 500 35 700 60 C900 85 1050 75 1200 58 L1200 100 L0 100 L0 100 Z" fill="#fff"/>
</svg>

<section>
  <div class="abs" style="left:75px;top:950px;width:325px;height:175px;border:2px solid var(--navy);border-right:none;border-bottom:none;border-radius:36px 36px 0 0"></div>
  <div class="abs" style="left:555px;top:1250px;width:43px;height:96px;border:2px solid var(--green);border-left:none;border-top:none"></div>
  <div class="abs photo" style="left:93px;top:972px;width:495px;height:362px;border-radius:40px" role="img" aria-label="Milk bottle, glass of milk and cheese on a wooden table in a sunny meadow"></div>
  <h2 class="abs section-title" style="left:625px;top:948px;font-size:46px">About<br>Verdale Trade</h2>
  <p class="abs body-text" style="left:625px;top:1070px;width:510px">Sed ut perspiciatis unde omnis iste natus error sit voluptatem accusantium doloremque laudantium, totam rem aperiam, eaque ipsa quae ab illo inventore veritatis et quasi architecto beatae vitae dicta sunt explicabo. Nemo enim ipsam voluptatem quia voluptas sit aspernatur aut odit aut fugit, sed quia consequuntur magni dolores eos qui ratione voluptatem sequi nesciunt.</p>
  <div class="abs" style="left:625px;top:1291px"><span class="btn" style="width:180px;height:54px;font-size:16px">Read More</span></div>
</section>

<div class="abs band" style="left:0;top:1440px;width:1200px;height:592px"></div>
<svg class="abs" style="left:0;top:1410px" width="1200" height="80" viewBox="0 0 1200 80">
  <path d="M0 0 H1200 V80 H0 Z" fill="#fff"/>
  <path d="M20 40 C250 10 450 20 700 50 C900 70 1050 40 1180 12 L1180 40 C1050 60 900 90 700 75 C450 45 250 40 20 70 Z" fill="var(--teal)"/>
  <path d="M20 70 C250 40 450 45 700 75 C900 90 1050 60 1180 40 L1200 80 L0 80 Z" fill="var(--teal-pale)"/>
</svg>
<h2 class="abs section-title" style="left:0;width:1200px;text-align:center;top:1540px;font-size:48px">Our Services</h2>
<p class="abs" style="left:0;width:1200px;text-align:center;top:1617px;font-size:15px;color:#444">Excepteur sint occaecat cupidatat non proident, sunt in culpa qui officia deserunt mollit anim id est laborum.</p>
<div class="service" style="left:75px;top:1677px"><div class="circle photo" role="img" aria-label="Toddler eating a dairy snack"></div><h3>Dairy Product Feeds</h3></div>
<div class="service" style="left:346px;top:1677px"><div class="circle" style="background:linear-gradient(135deg,#9fb4c8,#eef2f5,#5b7088)" role="img" aria-label="Milk bottles on a refrigerated shelf"></div><h3>Milk Products</h3></div>
<div class="service" style="left:617px;top:1677px"><div class="circle photo" role="img" aria-label="Fresh milk and cheese with cows grazing behind"></div><h3>Raw Milk Supply</h3></div>
<div class="service" style="left:885px;top:1677px"><div class="circle" style="background:linear-gradient(135deg,#5a3a28,#b88a5c,#7b6a52)" role="img" aria-label="Cows feeding in a dairy barn"></div><h3>Our Dairies</h3></div>

<h2 class="abs section-title" style="left:0;width:1200px;text-align:center;top:2078px;font-size:48px">Why Choose Us</h2>
<div class="why" style="left:75px;top:2189px"><div class="ring"><svg width="60" height="60" viewBox="0 0 60 60" fill="none" stroke="var(--blue)" stroke-width="2"><path d="M10 28 L36 16 V44 L10 32 Z"/><path d="M16 33 L20 46 H26 L23 35"/><circle cx="44" cy="20" r="7"/><path d="M44 16 V21 M44 23 V24"/></svg></div><h3>Attention</h3><p>Nemo enim ipsam volupta tem quia voluptas sit asp ernatur nulla.</p></div>
<div class="why" style="left:345px;top:2189px"><div class="ring"><svg width="60" height="60" viewBox="0 0 60 60" fill="none" stroke="var(--blue)" stroke-width="2"><path d="M8 34 L20 26 L30 32 L40 26 L52 34"/><path d="M20 26 L30 40 L40 32"/><circle cx="30" cy="16" r="7"/><path d="M27 16 l2 2 4-4"/></svg></div><h3>Commitment</h3><p>Nemo enim ipsam volupta tem quia voluptas sit asp ernatur nulla.</p></div>
<div class="why" style="left:617px;top:2189px"><div class="ring"><svg width="60" height="60" viewBox="0 0 60 60" fill="none" stroke="var(--blue)" stroke-width="2"><path d="M30 8 C40 18 46 26 46 36 A16 16 0 0 1 14 36 C14 28 20 22 24 16 C26 22 28 24 30 24 Z"/><path d="M24 34 h12 v10 h-12 z"/></svg></div><h3>Passionate</h3><p>Nemo enim ipsam volupta tem quia voluptas sit asp ernatur nulla.</p></div>
<div class="why" style="left:885px;top:2189px"><div class="ring"><svg width="60" height="60" viewBox="0 0 60 60" fill="none" stroke="var(--blue)" stroke-width="2"><path d="M10 24 L22 14 L30 20 L38 14 L50 24"/><path d="M20 28 V44 H40 V28"/><path d="M26 28 V20 M30 28 V18 M34 28 V20"/></svg></div><h3>Inclusive</h3><p>Nemo enim ipsam volupta tem quia voluptas sit asp ernatur nulla.</p></div>

<div class="abs band" style="left:0;top:2560px;width:1200px;height:520px"></div>
<svg class="abs" style="left:0;top:2515px" width="1200" height="80" viewBox="0 0 1200 80">
  <path d="M20 40 C250 10 450 20 700 50 C900 70 1050 40 1180 12 L1180 40 C1050 60 900 90 700 75 C450 45 250 40 20 70 Z" fill="var(--teal)"/>
  <path d="M20 70 C250 40 450 45 700 75 C900 90 1050 60 1180 40 L1200 80 L0 80 Z" fill="var(--teal-pale)"/>
</svg>
<h2 class="abs section-title" style="left:75px;top:2648px;font-size:48px">Message From<br>Manager</h2>
<p class="abs body-text" style="left:75px;top:2770px;width:500px;font-size:14.5px;line-height:32px">Sed ut perspiciatis unde omnis iste natus error sit voluptatem accusantium doloremque laudantium, totam rem aperiam, eaque ipsa quae ab illo inventore veritatis et quasi architecto beatae vitae dicta sunt explicabo..</p>
<div class="abs" style="left:75px;top:2930px"><span class="btn" style="width:178px;height:54px;font-size:16px">Read More</span></div>
<svg class="abs" style="left:670px;top:2618px" width="460" height="460" viewBox="0 0 460 460"><path d="M230 6 A224 224 0 0 1 454 230 A224 224 0 0 1 230 454" fill="none" stroke="var(--blue)" stroke-width="8"/></svg>
<div class="abs" style="left:676px;top:2621px;width:448px;height:448px;border-radius:50%;background:linear-gradient(160deg,#cfd9e3,#b8a487 55%,#6d7a4a)" role="img" aria-label="Farm manager standing in a field with cattle"></div>
<svg class="abs" style="left:0;top:3050px" width="1200" height="80" viewBox="0 0 1200 80">
  <path d="M0 0 H1200 V30 C1050 20 900 15 700 35 C450 55 250 45 0 60 Z" fill="var(--teal-pale)"/>
  <path d="M20 50 C250 30 450 40 700 25 C900 15 1050 30 1180 38 L1180 60 C1050 50 900 40 700 50 C450 60 250 60 20 80 Z" fill="var(--teal)"/>
</svg>

<h2 class="abs section-title" style="left:75px;top:3196px;font-size:48px">Latest News</h2>
<div class="abs" style="left:993px;top:3202px;width:134px;height:50px;border:2px solid var(--sky);border-radius:26px;display:flex;align-items:center;justify-content:center;font-size:16px;font-weight:600;color:var(--blue)">View All</div>
<article class="news" style="left:75px;top:3279px"><div class="thumb" style="background:linear-gradient(135deg,#c8b9a8,#eadccb,#7f8a94)" role="img" aria-label="Shopper checking her phone in the dairy aisle"></div><h3>Excepteur sint occaecat cupidatat</h3><div class="date">Jul, 20, 2023</div><p>Nemo enim ipsam voluptatem quia voluptas sit aspernatur aut odit aut fugit, sed quia consequuntur magni</p></article>
<article class="news" style="left:436px;top:3279px"><div class="thumb" style="background:linear-gradient(135deg,#3f3a36,#c9c2b8,#8a7d70)" role="img" aria-label="Fresh milk pouring from a steel pail"></div><h3>Excepteur sint occaecat cupidatat</h3><div class="date">Jul, 20, 2023</div><p>Nemo enim ipsam voluptatem quia voluptas sit aspernatur aut odit aut fugit, sed quia consequuntur magni</p></article>
<article class="news" style="left:797px;top:3279px"><div class="thumb" style="background:linear-gradient(135deg,#7a8796,#dfe6ec,#5b6675)" role="img" aria-label="Milk bottling line in a factory"></div><h3>Excepteur sint occaecat cupidatat</h3><div class="date">Jul, 20, 2023</div><p>Nemo enim ipsam voluptatem quia voluptas sit aspernatur aut odit aut fugit, sed quia consequuntur magni</p></article>

<div class="abs" style="left:0;top:3830px;width:1200px;height:620px;background:linear-gradient(180deg,#0a3f86,#0b2f66)" role="img" aria-label="Dark blue backdrop of cattle grazing"></div>
<svg class="abs" style="left:0;top:3790px" width="1200" height="80" viewBox="0 0 1200 80">
  <path d="M0 0 H1200 V30 C1000 20 800 40 600 35 C400 30 200 25 0 55 Z" fill="#fff"/>
  <path d="M20 50 C250 25 450 30 650 38 C850 45 1050 35 1180 18 L1180 45 C1050 55 850 60 650 55 C450 50 250 50 20 80 Z" fill="var(--teal)"/>
</svg>
<div class="abs" style="left:74px;top:3931px;width:448px;height:448px;border-radius:50%;border:8px solid var(--blue);background:linear-gradient(160deg,#9cc0e2,#d7dde3 45%,#5a6877)" role="img" aria-label="Dairy storage silos and milk tanker trucks"></div>
<h2 class="abs" style="left:580px;top:3962px;font-size:46px;font-weight:800;color:#fff">Quick Contact</h2>
<div class="field" style="left:580px;top:4045px;width:265px;height:48px">Name</div>
<div class="field" style="left:861px;top:4045px;width:265px;height:48px">Email Address</div>
<div class="field" style="left:580px;top:4108px;width:265px;height:48px">Phone No</div>
<div class="field" style="left:861px;top:4108px;width:265px;height:48px">Subject</div>
<div class="field" style="left:580px;top:4172px;width:546px;height:112px;border-radius:22px;align-items:flex-start;padding-top:16px">Message</div>
<div class="abs" style="left:580px;top:4300px"><span class="btn" style="width:178px;height:54px;font-size:16px">Submit Now</span></div>

<footer>
  <div class="abs brand" style="left:75px;top:4560px;font-size:36px"><span class="brand-mark"></span>Verdale Trade</div>
  <p class="abs" style="left:75px;top:4632px;font-size:13px;line-height:26px;color:#444">Copyrights© 2023 Company Name<br>All Rights Reserved</p>
  <div class="abs" style="left:75px;top:4698px;display:flex;gap:18px">
    <span class="social" aria-label="Social link"></span><span class="social" aria-label="Social link"></span><span class="social" aria-label="Social link"></span><span class="social" aria-label="Social link"></span><span class="social" aria-label="Social link"></span>
  </div>
  <div class="abs footer-col" style="left:395px;top:4505px"><h4>Site Map</h4><ul><li>Home</li><li>About Us</li><li>Service Offering</li><li>Products</li><li>Latest News</li><li>Contact Us</li></ul></div>
  <div class="abs footer-col" style="left:624px;top:4505px"><h4>Services</h4><ul><li>Excepteur sint</li><li>Occaecat cupidatat</li><li>Proidentsunt in culpa</li><li>Qui officia dese</li><li>Runt mollit</li></ul></div>
  <div class="abs footer-col" style="left:884px;top:4505px"><h4>Contact Info</h4>
    <div style="display:flex;gap:14px;font-size:14.5px;line-height:24px"><svg width="18" height="18" viewBox="0 0 24 24" style="margin-top:3px;flex:none"><path fill="var(--teal)" d="M12 2a7 7 0 0 0-7 7c0 5 7 13 7 13s7-8 7-13a7 7 0 0 0-7-7zm0 9.5A2.5 2.5 0 1 1 12 6.5a2.5 2.5 0 0 1 0 5z"/></svg><span>Suite 210<br>14 Orchard Lane, Elmvale<br>VIC 3999</span></div>
    <div style="display:flex;gap:14px;font-size:14.5px;margin-top:12px"><svg width="18" height="18" viewBox="0 0 24 24"><path fill="var(--teal)" d="M6.6 10.8a15 15 0 0 0 6.6 6.6l2.2-2.2c.3-.3.7-.4 1-.2 1.1.4 2.3.6 3.6.6.6 0 1 .4 1 1V20c0 .6-.4 1-1 1C10.6 21 3 13.4 3 4c0-.6.4-1 1-1h3.5c.6 0 1 .4 1 1 0 1.3.2 2.5.6 3.6.1.3 0 .7-.2 1z"/></svg><span>+61 3 5550 0142</span></div>
    <div style="display:flex;gap:14px;font-size:14.5px;margin-top:12px"><svg width="18" height="18" viewBox="0 0 24 24"><path fill="var(--teal)" d="M3 5h18v14H3z"/><path fill="none" stroke="#fff" stroke-width="2" d="M3 6l9 7 9-7"/></svg><span>sales@verdaletrade.com</span></div>
  </div>
  <div class="abs" style="left:1086px;top:4738px;width:56px;height:56px;border-radius:50%;background:linear-gradient(135deg,var(--mist),var(--sky))" role="img" aria-label="AI chat assistant button"></div>
</footer>

</body>
</html>
```